Professional IT Company Letterhead

We need a new letterhead design to incorporate our new login and business card design recently received here on Pixel Meadow. We want the same look and feel as the other two accepted projects. We want a professional and clean design.

Target Market(s)

Medical/Dental and Professional Services Businesses (CPA, Attorney, Architect etc)

Industry/Entity Type

Business

Requirements
Must have
• Clean and professional, consistent brand with our current design of our new logo and business cards.
Nice to have
• Would like to also be able to use the design on our newsletter header

```html
<!DOCTYPE html>
<html lang="en">
<head>
<meta charset="utf-8">
<title>Tidewell Technology Letterhead</title>
<link rel="stylesheet" href="https://fonts.googleapis.com/css2?family=Lato:wght@400;700&family=Montserrat:wght@400;600&display=swap">
<style>
  :root {
    --brand-blue: #1f8fd2;
    --sky-blue: #3aa8e2;
    --footer-grey: #5a5a5a;
    --water-deep: #3b93d0;
    --water-light: #cfe8f7;
    --paper: #ffffff;
  }
  * { margin: 0; padding: 0; box-sizing: border-box; }
  html, body { width: 848px; height: 1200px; overflow: hidden; background: var(--paper); }
  .letterhead {
    position: relative;
    width: 848px;
    height: 1200px;
    background: var(--paper);
    font-family: "Lato", Arial, sans-serif;
  }
  .brand {
    position: absolute;
    top: 40px;
    left: 0;
    width: 100%;
    text-align: center;
  }
  .brand-mark {
    display: inline-flex;
    align-items: center;
    gap: 10px;
  }
  .brand-dot {
    width: 34px;
    height: 34px;
    border-radius: 50%;
    background: var(--brand-blue);
  }
  .brand-name {
    font-family: "Montserrat", Arial, sans-serif;
    font-weight: 600;
    font-size: 28px;
    color: var(--brand-blue);
    line-height: 1;
  }
  .brand-tagline {
    margin-top: 16px;
    font-family: "Montserrat", Arial, sans-serif;
    font-weight: 400;
    font-size: 11.5px;
    letter-spacing: 1.2px;
    color: var(--sky-blue);
  }
  .water-band {
    position: absolute;
    left: 0;
    top: 1036px;
    width: 848px;
    height: 62px;
    background: linear-gradient(to bottom,
      rgba(207,232,247,0) 0%,
      var(--water-light) 30%,
      var(--water-deep) 55%,
      var(--water-light) 78%,
      rgba(207,232,247,0) 100%);
  }
  .contact {
    position: absolute;
    top: 1120px;
    left: 0;
    width: 100%;
    text-align: center;
    color: var(--footer-grey);
    font-size: 10px;
    line-height: 17px;
  }
  .contact-lines { display: inline-flex; gap: 16px; font-size: 13px; align-items: center; }
  .contact-line { display: inline-flex; align-items: center; gap: 7px; }
  .contact-icon { width: 12px; height: 12px; display: block; }
  .contact-web { color: var(--brand-blue); }
</style>
</head>
<body>
<div class="letterhead">
  <header class="brand">
    <div class="brand-mark">
      <span class="brand-dot"></span>
      <span class="brand-name">Tidewell Technology</span>
    </div>
    <p class="brand-tagline">IT Support for Medical &amp; Dental Practices</p>
  </header>

  <div class="water-band" role="img" aria-label="Photograph of splashing blue water spanning the page width"></div>

  <footer class="contact">
    <p>2870 Harbor Pines Road, Ste. B Lakemont, Texas 77512</p>
    <p class="contact-lines">
      <span class="contact-line">
        <svg class="contact-icon" viewBox="0 0 13 13" aria-hidden="true"><rect width="13" height="13" rx="2" fill="var(--brand-blue)"/><path d="M4 3 L5.5 3 L6 5 L5 5.8 C5.6 7 6.3 7.7 7.3 8.2 L8 7.2 L10 7.7 L10 9.3 C7 9.6 3.6 6.5 4 3 Z" fill="#fff"/></svg>
        555 014 2280
      </span>
      <span class="contact-line">
        <svg class="contact-icon" viewBox="0 0 13 13" aria-hidden="true"><rect width="13" height="13" rx="2" fill="var(--brand-blue)"/><rect x="3" y="5" width="7" height="4.5" rx="0.8" fill="#fff"/><rect x="4.2" y="3" width="4.6" height="2.4" fill="#fff"/></svg>
        555 014 2291
      </span>
    </p>
    <p>jordan@tidewellcomputers.com</p>
    <p class="contact-web">www.tidewellcomputers.com</p>
  </footer>
</div>
</body>
</html>
```